Modern and Clean Photograper´s Business Card

It´s a Personal Photographer´s business card that communicates elegance, modernity, efficiency.

Target Market(s)

people that wants an efficient and qualified photographer

Industry/Entity Type

Business

Contact Information for Business Card

modern, elegant, clean

Logo Text

TalvenKo fotografia

Font styles to use
Serif
Sans Serif
Script

Colors

Designer to choose colors to be used in the design.

Requirements
Must have
• one symbol per design.
• colors that match
Nice to have
• photography simbols like shutter, camera,movement.
• blended symbols like this designs: 15160747 and 5900864
Should not have
• logo symbol too big
• colors that don´t match
• loaded of symbols, and looks like bloated.

```html
<!DOCTYPE html>
<html lang="en">
<head>
<meta charset="utf-8">
<title>TalvenKo Photography – Business Card</title>
<link href="https://fonts.googleapis.com/css2?family=Montserrat:wght@500;600;700&display=swap" rel="stylesheet">
<style>
  :root {
    --backdrop: #d9d6d0;
    --card: #f2f2f2;
    --card-edge: #e2e2e2;
    --ink: #3d3d3f;
    --wine: #7e1a27;
    --muted: #4a4a4c;
  }
  * { box-sizing: border-box; margin: 0; padding: 0; }
  html, body {
    width: 1200px; height: 800px; overflow: hidden;
    background: var(--backdrop);
    font-family: "Montserrat", sans-serif;
  }
  .canvas { position: relative; width: 1200px; height: 800px; }
  .card {
    position: absolute;
    width: 525px; height: 300px;
    background: linear-gradient(135deg, #fafafa, var(--card) 60%, var(--card-edge));
    box-shadow: 0 10px 26px rgba(0,0,0,.22);
    overflow: hidden;
  }
  .card--front { left: 50px; top: 130px; }
  .card--back  { left: 625px; top: 370px; }

  .wordmark {
    position: absolute; left: 0; right: 0; top: 108px;
    text-align: center;
  }
  .wordmark__name {
    font-weight: 700; font-size: 54px; letter-spacing: -1px;
    color: var(--ink); line-height: 1;
  }
  .wordmark__tag {
    display: block; margin-top: 4px; padding-left: 170px;
    font-weight: 600; font-size: 22px; color: var(--wine);
  }

  .accent-disc {
    position: absolute; right: -70px; top: -150px;
    width: 330px; height: 330px; border-radius: 50%;
    background: var(--wine);
  }
  .holder { position: absolute; left: 36px; top: 150px; }
  .holder__name { font-weight: 700; font-size: 22px; color: var(--ink); }
  .holder__role { font-weight: 600; font-size: 18px; color: var(--wine); margin-top: 2px; }

  .contacts {
    position: absolute; left: 250px; top: 176px;
    list-style: none;
  }
  .contacts__item {
    display: flex; align-items: center; gap: 9px;
    font-weight: 500; font-size: 13px; color: var(--muted);
    height: 26px;
  }
  .contacts__icon {
    width: 18px; height: 18px; border-radius: 3px;
    background: var(--ink);
    display: flex; align-items: center; justify-content: center;
    flex: none;
  }
  .contacts__icon svg { width: 12px; height: 12px; }
</style>
</head>
<body>
<main class="canvas">
  <section class="card card--front" aria-label="Card front">
    <div class="wordmark">
      <div class="wordmark__name">TalvenKo</div>
      <span class="wordmark__tag">Photography</span>
    </div>
  </section>

  <section class="card card--back" aria-label="Card back">
    <div class="accent-disc"></div>
    <div class="holder">
      <p class="holder__name">Talven Korrin</p>
      <p class="holder__role">Owner</p>
    </div>
    <ul class="contacts">
      <li class="contacts__item">
        <span class="contacts__icon"><svg viewBox="0 0 12 12"><rect x="3" y="1" width="6" height="10" rx="1" fill="none" stroke="#fff" stroke-width="1.4"/></svg></span>
        555 . 018 . 2290
      </li>
      <li class="contacts__item">
        <span class="contacts__icon"><svg viewBox="0 0 12 12"><rect x="1" y="2.5" width="10" height="7" fill="none" stroke="#fff" stroke-width="1.2"/><path d="M1 2.5 6 7l5-4.5" fill="none" stroke="#fff" stroke-width="1.2"/></svg></span>
        info@talvenkophoto.com
      </li>
      <li class="contacts__item">
        <span class="contacts__icon"><svg viewBox="0 0 12 12"><circle cx="6" cy="6" r="4.8" fill="none" stroke="#fff" stroke-width="1.1"/><path d="M1.2 6h9.6M6 1.2v9.6" stroke="#fff" stroke-width="1"/><ellipse cx="6" cy="6" rx="2.2" ry="4.8" fill="none" stroke="#fff" stroke-width="1"/></svg></span>
        www.talvenkophoto.com
      </li>
      <li class="contacts__item">
        <span class="contacts__icon"></span>
        @talvenkofoto
      </li>
    </ul>
  </section>
</main>
</body>
</html>
```